Plomberie TRD est une nouvelle entreprise de plomberie

Jaimerais maintenant des carte daffaire

Tendance
Avec un petit Puntch

Jaimerais quelque chose dans ce style avec le logo foncé plomberie trd en facade
Jaimerais une photo en backgroung de fitting de plomberie comme je vous ai envoyer

Si vous voulez chercher une photo marquer sur google ( fitting kopran) pour vous donner des idee
Je veux que les fitting soit dune couleur pale en back ground pour faire ressortir mon logo

Toujours en facade de la carte je veux quil y ai mes services d'inscrit

Construction neuve
Reparation
Renovation
Urgence

438-261-5907
Bastien corriveau

A larriere de la carte jaimerais le logo pâle plomberie TRD
Avec mes info
Email: info.trdbatiment@exemplemail.com
Bastien corriveau
Cell: 438-261-5907
Plomberietrd.example

Voici des design que jai bien aimer libre a vous de vous laisser aller plus loin

Merci au plaisir de travailler avec vous

Target Market(s)

30 a 60 ans contracteur general

Industry/Entity Type

Construction plomberie

Contact Information for Business Card

Plomberie TRD inc. 438-261-5907 Bastien corriveau. Plombier. info.trdbatiment@exemplemail.com

Font styles to use
Sans Serif

Colors
0054AA
0677BA
7BADD7
CADEEF
E8F1F8
F0912C
F2A743
F7CA91
FBE8D2
FDF5EE
EE7325
F08F49
F5BC92
FAE3D3
FDF4ED

Requirements
Must have
• Plombier serieux et virile jaime la couleur cuivre comme les fitting
Nice to have
• Carte transparente

```html
<!DOCTYPE html>
<html lang="fr">
<head>
<meta charset="utf-8">
<title>Plomberie TRD – Carte d'affaires</title>
<link href="https://fonts.googleapis.com/css2?family=Open+Sans:wght@400;600;700;800&display=swap" rel="stylesheet">
<style>
  :root {
    --page: #e6ebf0;
    --ink-dark: #1f2328;
    --ink-dark-2: #3a3f45;
    --blue-deep: #0054AA;
    --blue: #0677BA;
    --blue-name: #2f7fc9;
    --blue-soft: #7BADD7;
    --copper: #c9621f;
    --copper-light: #EE7325;
    --white: #ffffff;
    --text-light: #e9ecef;
    --text-muted: #c4c9cf;
    --face-light: #f3f5f7;
    --face-mist: #d9e1ea;
  }
  * { margin: 0; padding: 0; box-sizing: border-box; }
  html, body {
    width: 1200px; height: 780px; overflow: hidden;
    background: var(--page);
    font-family: "Open Sans", sans-serif;
  }
  .business-card {
    position: absolute; left: 60px; top: 93px;
    width: 1080px; height: 594px; overflow: hidden;
    background: linear-gradient(180deg, var(--face-light) 0%, var(--white) 40%, var(--face-mist) 100%);
    box-shadow: 0 10px 30px rgba(0,0,0,.18);
  }
  .card-shapes { position: absolute; inset: 0; }
  .name-bar {
    position: absolute; left: 2px; top: 35px; width: 32px; height: 90px;
    background: linear-gradient(90deg, var(--blue-deep), var(--blue));
  }
  .holder-name {
    position: absolute; left: 42px; top: 34px;
    font-size: 48px; font-weight: 700; line-height: 1; letter-spacing: .5px;
    white-space: nowrap;
  }
  .holder-name .first { color: var(--blue-name); }
  .holder-name .last { color: var(--copper-light); }
  .holder-role {
    position: absolute; left: 44px; top: 90px;
    font-size: 26px; font-weight: 600; color: var(--white);
  }
  .services-title {
    position: absolute; left: 44px; top: 210px;
    font-size: 30px; font-weight: 700; color: var(--blue-name); letter-spacing: .5px;
  }
  .services-list {
    position: absolute; left: 44px; top: 268px; list-style: none;
  }
  .services-list li {
    position: relative; padding-left: 26px;
    font-size: 27px; line-height: 35.5px; color: var(--text-light);
  }
  .services-list li::before {
    content: ""; position: absolute; left: 0; top: 10px;
    width: 15px; height: 15px; border-radius: 50%; background: var(--white);
  }
  .contact-list { position: absolute; left: 44px; top: 448px; list-style: none; }
  .contact-list li {
    display: flex; align-items: center; gap: 14px;
    font-size: 26px; line-height: 35.5px; color: var(--text-muted); white-space: nowrap;
  }
  .contact-list .icon { width: 24px; height: 24px; flex: none; }
  .contact-list .no-icon { padding-left: 38px; }
  .brand-name {
    position: absolute; left: 615px; top: 222px; width: 430px;
    text-align: center; color: var(--blue-deep); font-weight: 800; line-height: 1;
  }
  .brand-name .word-small { display: block; font-size: 30px; letter-spacing: 15px; margin-bottom: 14px; padding-left: 15px; }
  .brand-name .word-large { display: block; font-size: 118px; letter-spacing: 6px; }
</style>
</head>
<body>
  <section class="business-card">
    <svg class="card-shapes" viewBox="0 0 1080 594" width="1080" height="594" aria-hidden="false">
      <defs>
        <linearGradient id="fittingsTone" x1="0" y1="0" x2="1" y2="1">
          <stop offset="0" stop-color="#2a2e33"/>
          <stop offset=".5" stop-color="#3b4046"/>
          <stop offset="1" stop-color="#24282d"/>
        </linearGradient>
        <linearGradient id="blueSweep" x1="0" y1="0" x2="0" y2="1">
          <stop offset="0" stop-color="#0677BA"/>
          <stop offset="1" stop-color="#0054AA"/>
        </linearGradient>
        <linearGradient id="copperSweep" x1="0" y1="0" x2="0" y2="1">
          <stop offset="0" stop-color="#8a3f12"/>
          <stop offset=".5" stop-color="#c9621f"/>
          <stop offset="1" stop-color="#8a3f12"/>
        </linearGradient>
      </defs>
      <path role="img" aria-label="Photo en arrière-plan de raccords de plomberie à sertir et de pinces, en tons sombres"
            d="M0,0 L670,0 Q444,300 590,594 L0,594 Z" fill="url(#fittingsTone)"/>
      <path class="blue-arc" d="M733,0 Q555,190 582,400 Q572,200 682,0 Z" fill="url(#blueSweep)"/>
      <path class="copper-arc" d="M566,233 Q515,420 644,594 L672,594 Q548,420 566,233 Z" fill="url(#copperSweep)"/>
    </svg>

    <div class="name-bar"></div>
    <h1 class="holder-name"><span class="first">Bastien</span> <span class="last">Corriveau</span></h1>
    <p class="holder-role">Plombier</p>

    <h2 class="services-title">SERVICES</h2>
    <ul class="services-list">
      <li>Repair</li>
      <li>Renovation</li>
      <li>Emergency</li>
      <li>New construction</li>
    </ul>

    <ul class="contact-list">
      <li>
        <svg class="icon" viewBox="0 0 24 24"><path d="M6.6 10.8a15 15 0 0 0 6.6 6.6l2.2-2.2a1 1 0 0 1 1-.25 11.4 11.4 0 0 0 3.6.57 1 1 0 0 1 1 1V20a1 1 0 0 1-1 1A17 17 0 0 1 3 4a1 1 0 0 1 1-1h3.5a1 1 0 0 1 1 1c0 1.25.2 2.45.57 3.57a1 1 0 0 1-.25 1z" fill="#aeb5bd"/></svg>
        <span>438-261-5907</span>
      </li>
      <li>
        <svg class="icon" viewBox="0 0 24 24"><circle cx="12" cy="12" r="10" fill="#F08F49"/><path d="M2 12h20M12 2c3 3 3 17 0 20M12 2c-3 3-3 17 0 20" stroke="#fff" stroke-width="1.4" fill="none"/></svg>
        <span>www.plomberietrd.example</span>
      </li>
      <li class="no-icon"><span>info.trdbatiment@exemplemail.com</span></li>
    </ul>

    <p class="brand-name"><span class="word-small">PLOMBERIE</span><span class="word-large">TRD</span></p>
  </section>
</body>
</html>
```